- Redesign our business card
- Logo remains unchanged
- Current business card attached

Target Market(s)

We are a property management company

Industry/Entity Type

Business

```html
<!DOCTYPE html>
<html lang="en">
<head>
<meta charset="utf-8">
<title>Harlow Property Group – Business Card</title>
<link rel="stylesheet" href="https://fonts.googleapis.com/css2?family=Roboto:wght@400&family=Roboto+Condensed:wght@400;500&display=swap">
<style>
  :root {
    --slate: #59676d;
    --slate-soft: #7a8b92;
    --olive: #8fa64a;
    --olive-deep: #6f7f1e;
    --sand: #e6dfb6;
    --sand-pale: #f8f8ea;
    --sage-pale: #e4ebd6;
    --mist: #dfe6e5;
    --ink: #2b3338;
    --ink-soft: #4d5a60;
    --paper: #ffffff;
  }
  html, body {
    margin: 0;
    padding: 0;
    width: 1200px;
    height: 764px;
    overflow: hidden;
    background: var(--paper);
  }
  .canvas {
    position: relative;
    width: 1200px;
    height: 764px;
  }
  .card {
    position: absolute;
    top: 70px;
    width: 373px;
    height: 610px;
    background: var(--paper);
    border: 1px solid var(--slate);
    box-sizing: border-box;
    overflow: hidden;
  }
  .card--front { left: 189px; }
  .card--back  { left: 626px; }
  .card svg.backdrop {
    position: absolute;
    inset: 0;
  }
  .brand {
    position: absolute;
    left: 24px;
    top: 222px;
    display: flex;
    align-items: center;
    gap: 8px;
    font-family: "Roboto Condensed", Arial, sans-serif;
    font-weight: 500;
    font-size: 22px;
    letter-spacing: 0.2px;
    color: var(--slate);
    margin: 0;
  }
  .brand__mark {
    width: 14px;
    height: 14px;
    background: var(--olive);
  }
  .holder {
    position: absolute;
    right: 34px;
    top: 446px;
    text-align: right;
    font-family: "Roboto Condensed", Arial, sans-serif;
  }
  .holder__name {
    margin: 0;
    font-size: 22px;
    font-weight: 500;
    color: var(--ink);
    letter-spacing: 0.3px;
  }
  .holder__role {
    margin: 8px 0 0;
    font-size: 18px;
    font-weight: 500;
    color: var(--ink-soft);
  }
  .contact {
    position: absolute;
    left: 21px;
    top: 404px;
    margin: 0;
    padding: 0;
    list-style: none;
    font-family: "Roboto", Arial, sans-serif;
    font-size: 13.4px;
    color: var(--ink);
    line-height: 23px;
  }
  .services {
    position: absolute;
    left: 0;
    right: 0;
    top: 552px;
    margin: 0;
    text-align: center;
    font-family: "Roboto Condensed", Arial, sans-serif;
    font-size: 14px;
    line-height: 22px;
    color: var(--olive-deep);
  }
</style>
</head>
<body>
<main class="canvas">

  <section class="card card--front" aria-label="Card front">
    <svg class="backdrop" width="373" height="610" viewBox="0 0 373 610">
      <defs>
        <linearGradient id="front-wash" x1="0" y1="0" x2="1" y2="0">
          <stop offset="0" stop-color="var(--sand-pale)"/>
          <stop offset="0.75" stop-color="var(--sage-pale)"/>
          <stop offset="1" stop-color="var(--mist)"/>
        </linearGradient>
      </defs>
      <rect x="0" y="40" width="373" height="380" fill="url(#front-wash)" role="img" aria-label="Soft brand colour panel"/>
      <polygon points="0,0 373,0 373,14 0,40" fill="var(--slate)"/>
      <polygon points="0,598 373,572 373,610 0,610" fill="var(--slate)"/>
    </svg>
    <p class="brand"><span class="brand__mark"></span>HARLOW PROPERTY GROUP</p>
    <div class="holder">
      <p class="holder__name">DANIEL HARLOW</p>
      <p class="holder__role">Licensed Strata Manager</p>
    </div>
  </section>

  <section class="card card--back" aria-label="Card back">
    <svg class="backdrop" width="373" height="610" viewBox="0 0 373 610">
      <defs>
        <linearGradient id="back-wash" x1="0" y1="0" x2="1" y2="0">
          <stop offset="0" stop-color="var(--slate-soft)"/>
          <stop offset="0.55" stop-color="var(--olive)"/>
          <stop offset="1" stop-color="var(--sand)"/>
        </linearGradient>
      </defs>
      <polygon points="0,0 373,0 373,215 190,320 0,388" fill="url(#back-wash)" role="img" aria-label="Brand colour panel in slate, olive and sand"/>
    </svg>
    <ul class="contact">
      <li>PO BOX 48, ELMWOOD VALE NSW 2090</li>
      <li>12/6—18 CARROW LANE ELMWOOD NSW 2091</li>
      <li>T: 02 9000 1234 &nbsp; F: 02 9000 5678 &nbsp; M: 0400 555 019</li>
      <li>E: info@harlowproperty.example</li>
      <li>www.harlowproperty.example</li>
    </ul>
    <p class="services">Strata Management &nbsp;|&nbsp; Community Management &nbsp;|<br>Property Management</p>
  </section>

</main>
</body>
</html>
```